Kitchen and Bathroom Remodeling Flyer

This flyer is for a home remodeling company that remodels peoples kitchens and bathrooms.

We want a flyer to be sophisticated: nice professional design with classy font.

FRONT OF FLYER:

I have attached the front flyer I created and there is no design to it. The reason is so you can see what text elements we want on the flyer. a second attachment has the text for easy copy and paste.

I like the idea of mentioning “Owners live in Ahwatukee” because this flyer will be passed around door to door in that town of Ahwatukee.

Please use the image and the corresponding headline specific to that image. The headline can be in the image or to the top of the image.

BACK OF FLYER:
The back of flyer is essentially a written letter with a profile image of our owners and then two testimonials at bottom. I’d like to add a little bit of design to the back of the flyer. See attachment for pdf of current text and basic structure.

Our brand colors are gray and blue# 0000cc

Our website is https://Kelmbrookrenovating.com

Thank you,
Tobias

Target Market(s)

Mostly woman. Homeowners making 100k+ a year that want to remodel their kitchen or bathroom

Industry/Entity Type

Home Improvement

Font styles to use
Serif
Sans Serif
Decorative

Colors

Designer to choose colors to be used in the design.

Requirements
Must have
• This has to be in photoshop with each element editable (I’ll want to change things down the road)
Nice to have
• Examples that I don’t want copied but so you have a rough idea of some design structure that I like:
• https://flyer.pixelvantyard.com/contest.aspx?id=5190362
• https://flyer.pixelvantyard.com/contest.aspx?id=627053
• https://flyer.pixelvantyard.com/contest.aspx?id=8831475
• https://www.pixelvantyard.com/design/42957018
• https://www.pixelvantyard.com/design/7160243
Should not have
• Nothing silly or too loud. Thank you

```html
<!DOCTYPE html>
<html lang="en">
<head>
<meta charset="utf-8">
<title>Kelmbrook Renovating Flyer</title>
<link href="https://fonts.googleapis.com/css2?family=Oswald:wght@500;600&family=Open+Sans:wght@400;600;700&family=Playfair+Display:ital,wght@1,700&display=swap" rel="stylesheet">
<style>
  :root {
    --blue: #2a45a8;
    --blue-deep: #1f3a9e;
    --blue-band: #3a5bb8;
    --gold: #f3c01c;
    --ink: #3b3b3b;
    --heading: #2b2b2b;
    --paper: #ffffff;
    --backdrop: #e3e4e6;
  }
  * { box-sizing: border-box; margin: 0; padding: 0; }
  html, body { width: 1200px; height: 900px; overflow: hidden; background: var(--backdrop); }
  body { position: relative; font-family: "Open Sans", sans-serif; color: var(--ink); }

  .page {
    position: absolute; top: 100px; width: 540px; height: 700px;
    background: var(--paper); overflow: hidden;
    box-shadow: 0 8px 24px rgba(0,0,0,.12);
  }
  .page--front { left: 45px; }
  .page--back { left: 615px; }

  .hero-photo { position: absolute; left: 0; top: 0; width: 100%; }
  .page--front .hero-photo { height: 350px; background: linear-gradient(160deg, #f4f4f2 0%, #dcdad6 45%, #b9b2a8 100%); }
  .page--back .hero-photo { height: 270px; background: linear-gradient(150deg, #ece8e2 0%, #b8aa9a 50%, #7d6c5e 100%); }

  .headline {
    position: absolute; font-family: "Oswald", sans-serif; font-weight: 600;
    text-transform: uppercase; color: var(--blue); line-height: 1.08;
  }
  .page--front .headline { left: 34px; top: 70px; font-size: 33px; }
  .page--back .headline { left: 34px; top: 50px; font-size: 31px; }

  .wave { position: absolute; left: 0; width: 100%; display: block; }

  .promise { position: absolute; left: 34px; top: 394px; width: 282px; }
  .section-title {
    font-family: "Oswald", sans-serif; font-weight: 500; font-size: 20px;
    text-transform: uppercase; color: var(--heading); border-left: 4px solid var(--blue);
    padding-left: 8px; margin-bottom: 12px; line-height: 1;
  }
  .promise ul { list-style: none; font-size: 10px; line-height: 1.55; }
  .promise li::before { content: "• "; }

  .feature { position: absolute; right: 26px; top: 380px; width: 196px; text-align: center; }
  .feature-title {
    font-family: "Oswald", sans-serif; font-weight: 500; font-size: 15px;
    text-transform: uppercase; color: var(--heading); line-height: 1.15; margin-bottom: 10px;
  }
  .feature-photo {
    width: 186px; height: 118px; margin: 0 auto; border: 4px solid #fff;
    box-shadow: 0 1px 4px rgba(0,0,0,.25);
    background: linear-gradient(180deg, #cfc9c2 0%, #6b5a4c 60%, #4a3c32 100%);
  }

  .letter { position: absolute; left: 34px; top: 292px; width: 472px; }
  .greeting {
    font-family: "Playfair Display", serif; font-style: italic; font-weight: 700;
    font-size: 23px; color: var(--heading); border-left: 4px solid var(--blue);
    padding-left: 8px; margin-bottom: 10px; line-height: 1.1;
  }
  .letter p { font-size: 9.4px; line-height: 1.55; }

  .footer-bg { position: absolute; left: 0; bottom: 0; width: 100%; }

  .contact { position: absolute; left: 28px; bottom: 22px; display: flex; align-items: center; gap: 12px; }
  .avatar {
    width: 64px; height: 64px; border-radius: 50%; border: 3px solid #fff; flex: none;
    background: radial-gradient(circle at 50% 40%, #c99a7e 0%, #7a5a48 60%, #2d4a9a 100%);
  }
  .contact-label { font-family: "Oswald", sans-serif; font-size: 8px; text-transform: uppercase; color: #fff; }
  .contact-name { font-family: "Oswald", sans-serif; font-weight: 500; font-size: 17px; color: var(--gold); text-transform: uppercase; line-height: 1.1; white-space: nowrap; }
  .contact-phone { font-size: 10px; font-weight: 700; color: #fff; display: flex; align-items: center; gap: 6px; margin-top: 3px; }

  .divider { position: absolute; left: 326px; bottom: 24px; width: 1px; height: 62px; background: rgba(255,255,255,.35); }

  .company { position: absolute; right: 20px; bottom: 26px; width: 186px; text-align: center; font-size: 8.3px; line-height: 1.55; color: #fff; white-space: nowrap; }
  .company-name { display: flex; align-items: center; justify-content: center; gap: 6px; font-family: "Playfair Display", serif; font-style: italic; font-weight: 700; font-size: 15px; margin-bottom: 3px; }
  .company-name::before { content: ""; width: 9px; height: 9px; background: #fff; }
</style>
</head>
<body>

<!-- FRONT -->
<section class="page page--front">
  <div class="hero-photo" role="img" aria-label="Bright white kitchen with marble island set with pastries and flowers"></div>
  <h1 class="headline">Entertain in a kitchen<br>you’ll love showing off<br>to friends &amp; family</h1>

  <svg class="wave" style="top:290px" width="540" height="90" viewBox="0 0 540 90" preserveAspectRatio="none">
    <path d="M0 60 C140 95 300 10 540 20 L540 90 L0 90 Z" fill="var(--blue-deep)"/>
    <path d="M0 70 C150 100 310 22 540 30 L540 90 L0 90 Z" fill="#fff"/>
  </svg>

  <div class="promise">
    <h2 class="section-title">Our client promise:</h2>
    <ul>
      <li>Provide honest and straight forward advice</li>
      <li>Return calls and show up on time</li>
      <li>Employ professional, respectful and knowledgeable employees</li>
      <li>Respect your home and ensure we keep it clean</li>
      <li>Respect the expectations of project timelines and deadlines</li>
      <li>Deliver your dream living space with great attention to detail</li>
    </ul>
  </div>

  <div class="feature">
    <h3 class="feature-title">Turn an old bathroom into<br>your own personal spa</h3>
    <div class="feature-photo" role="img" aria-label="Remodeled bathroom with dark wood double vanity and mirrors"></div>
  </div>

  <svg class="footer-bg" width="540" height="140" viewBox="0 0 540 140" preserveAspectRatio="none">
    <path d="M0 42 C170 30 350 20 540 0 L540 140 L0 140 Z" fill="var(--blue-deep)"/>
    <path d="M0 126 L540 110 L540 140 L0 140 Z" fill="var(--blue-band)"/>
  </svg>

  <div class="contact">
    <div class="avatar" role="img" aria-label="Portrait of co-founder"></div>
    <div>
      <div class="contact-label">Contact</div>
      <div class="contact-name">Tobias, Walter and Curtis</div>
      <div class="contact-phone">
        <svg width="8" height="12" viewBox="0 0 8 12"><rect x="0.5" y="0.5" width="7" height="11" rx="1.5" fill="none" stroke="#fff"/><circle cx="4" cy="9.5" r=".8" fill="#fff"/></svg>
        555-318-4072
      </div>
    </div>
  </div>
  <div class="divider"></div>
  <div class="company">
    <div class="company-name">Kelmbrook Renovating</div>
    Kelmbrook Renovating 555-318-4072<br>
    ROC# 480127 Kelmbrookrenovating.com<br>
    LICENSED | BONDED | INSURED
  </div>
</section>

<!-- BACK -->
<section class="page page--back">
  <div class="hero-photo" role="img" aria-label="Spa bathroom with freestanding white tub and glass shower"></div>
  <h1 class="headline">Turn an old bathroom into<br>your own personal spa</h1>

  <svg class="wave" style="top:200px" width="540" height="100" viewBox="0 0 540 100" preserveAspectRatio="none">
    <path d="M0 70 C150 5 330 70 540 10 L540 100 L0 100 Z" fill="var(--blue-deep)"/>
    <path d="M0 80 C150 15 330 80 540 20 L540 100 L0 100 Z" fill="#fff"/>
  </svg>

  <div class="letter">
    <h2 class="greeting">Dear Ahwatukee Homeowners,</h2>
    <p>Everyone wants a dream home they can be proud of. We all want to feel prosperous in life and our home is an extension of ourselves, our style and feeling successful.</p>
    <p>We understand working with a remodeling contractor can be frustrating because they show up late, change the price and make a mess of your home.</p>
    <p>Kelmbrook Renovating is the most organized remodeling company in the valley and we’ll create the dream space you’ll be proud to show off to your friends, family, &amp; neighbors.</p>
    <p>One of our co-founders Tobias has been through several contractor nightmares and it is the main reason Tobias, Walter and Curtis founded Kelmbrook Renovating.</p>
    <p>We are an award-winning home remodeling licensed contractor that is known for showing up on time, being organized, clearly explaining all aspects of the remodel, adhering to project budget and timeline.</p>
    <p>One of our client’s said we were the AutoVale of home remodeling and we think that’s a nice comparison. We’ll guide you through our 4 step process and there’s no haggle, no sales BS and our clients love the experience.</p>
  </div>

  <svg class="footer-bg" width="540" height="130" viewBox="0 0 540 130" preserveAspectRatio="none">
    <path d="M0 60 C180 50 360 40 540 0 L540 130 L0 130 Z" fill="var(--blue-deep)"/>
    <path d="M0 116 L540 100 L540 130 L0 130 Z" fill="var(--blue-band)"/>
  </svg>

  <div class="contact">
    <div class="avatar" role="img" aria-label="Portrait of co-founder"></div>
    <div>
      <div class="contact-label">Contact</div>
      <div class="contact-name">Tobias, Walter and Curtis</div>
      <div class="contact-phone">
        <svg width="8" height="12" viewBox="0 0 8 12"><rect x="0.5" y="0.5" width="7" height="11" rx="1.5" fill="none" stroke="#fff"/><circle cx="4" cy="9.5" r=".8" fill="#fff"/></svg>
        555-318-4072
      </div>
    </div>
  </div>
  <div class="divider"></div>
  <div class="company">
    <div class="company-name">Kelmbrook Renovating</div>
    Kelmbrook Renovating 555-318-4072<br>
    ROC# 480127 Kelmbrookrenovating.com<br>
    LICENSED | BONDED | INSURED
  </div>
</section>

</body>
</html>
```